Yoga Studio Postcard Advertising Flyer

Need a postcard size flyer that will promote our business. The objective is to promote location and availability. Want it to be personal. The objective to connect the audience to the purpose of yoga and the focus on enabling functional well-being. Something that is a very big focus at this point in time in the world. I really want people to see the value in connecting with us via our website, classora app, linkhive or pixly. The colours are to be bright but not overwhelming and aligned to the logo colours. Its also important to have the location picture on the flyer - unless you think that it is way too much (try a with or without). I don't want this to be a specials brochure - it is an introduction to our brand and our business. No need to over do it with promotional lines apart from come and join us.
Updates

Delayed in organising this.

Target Market(s)

Local yogis and residence who are or want to be focused on well-being.

Requirements
Must have
• Pictures - would have the logo on one side.
Nice to have
• Modern and aligned to website design.

```html
<!DOCTYPE html>
<html lang="en">
<head>
<meta charset="utf-8">
<title>Amber Lily Yoga – Postcard Flyer</title>
<link rel="stylesheet" href="https://fonts.googleapis.com/css2?family=Roboto:wght@400;500&family=Roboto+Condensed:wght@500&family=Kaushan+Script&display=swap">
<style>
  :root {
    --navy: #1d2a5a;
    --sky: #29a6e0;
    --deep: #1a2d66;
    --paper: #eef0f2;
    --white: #ffffff;
    --floor-dark: #2a221d;
    --floor-warm: #6b4a32;
  }
  * { margin: 0; padding: 0; box-sizing: border-box; }
  html, body { width: 1200px; height: 800px; overflow: hidden; background: var(--paper); }
  .postcard {
    position: relative;
    width: 1200px;
    height: 800px;
    overflow: hidden;
    background: var(--paper);
    font-family: "Roboto", Arial, sans-serif;
    color: var(--navy);
  }
  .backdrop { position: absolute; inset: 0; }
  .contact { position: absolute; left: 24px; top: 66px; }
  .contact__web { font-size: 22px; font-weight: 500; letter-spacing: 0.2px; }
  .contact__find { margin-top: 16px; font-size: 17px; font-weight: 500; display: flex; gap: 14px; align-items: baseline; }
  .contact__channel { font-size: 19px; font-weight: 500; color: var(--navy); }
  .rule { position: absolute; left: 0; width: 330px; height: 2px; background: linear-gradient(90deg, var(--sky), rgba(41,166,224,0)); }
  .rule--top { top: 56px; }
  .rule--bottom { top: 170px; }
  .brand {
    position: absolute; left: 372px; top: 128px; width: 230px;
    text-align: center; font-size: 27px; font-weight: 500; letter-spacing: 1px; line-height: 1.25;
    color: var(--navy);
  }
  .portrait {
    position: absolute; left: 26px; top: 212px; width: 118px; height: 154px;
    background: linear-gradient(180deg, #cfd3d6, #8e9499);
  }
  .values { position: absolute; left: 166px; top: 220px; list-style: none; width: 400px; }
  .values__item { position: relative; padding-left: 40px; font-size: 18px; line-height: 1.2; margin-bottom: 10px; }
  .values__item::before {
    content: ""; position: absolute; left: 4px; top: 5px; width: 20px; height: 20px;
    border-radius: 50%; background: var(--navy);
  }
  .vision { position: absolute; left: 24px; top: 386px; width: 380px; font-size: 20px; line-height: 1.3; }
  .invite {
    position: absolute; left: 26px; top: 496px;
    font-family: "Kaushan Script", cursive; font-size: 40px; color: var(--navy);
    transform: rotate(-13deg); transform-origin: left center;
  }
  .headline {
    position: absolute; left: 562px; top: 488px;
    font-family: "Roboto Condensed", "Arial Narrow", sans-serif; font-weight: 500;
    color: var(--white); line-height: 0.98;
  }
  .headline__lead { display: block; font-size: 136px; letter-spacing: 1px; }
  .headline__sub { display: block; font-size: 80px; letter-spacing: 0.5px; }
</style>
</head>
<body>
<main class="postcard">
  <svg class="backdrop" width="1200" height="800" viewBox="0 0 1200 800">
    <defs>
      <linearGradient id="chapel-tone" x1="0" y1="0" x2="1" y2="0">
        <stop offset="0" stop-color="#e4e7ea"/>
        <stop offset="1" stop-color="#f4f5f6"/>
      </linearGradient>
      <linearGradient id="class-tone" x1="0" y1="0" x2="1" y2="1">
        <stop offset="0" stop-color="#f3f5f7"/>
        <stop offset="0.6" stop-color="#b9c2cb"/>
        <stop offset="1" stop-color="#3a3f46"/>
      </linearGradient>
      <linearGradient id="studio-tone" x1="0" y1="0" x2="1" y2="0">
        <stop offset="0" stop-color="var(--floor-warm)"/>
        <stop offset="0.45" stop-color="var(--floor-dark)"/>
        <stop offset="0.7" stop-color="#2b2b2b"/>
        <stop offset="1" stop-color="#8a8a8a"/>
      </linearGradient>
    </defs>
    <g role="img" aria-label="Faint photo of the chapel studio building">
      <rect x="0" y="0" width="760" height="600" fill="url(#chapel-tone)"/>
    </g>
    <g role="img" aria-label="Photo of yoga students holding a warrior pose on mats">
      <path d="M760 0 L1200 0 L1200 330 C1080 300 960 330 850 330 C720 260 700 120 760 0 Z" fill="url(#class-tone)"/>
    </g>
    <g role="img" aria-label="Photo of the wooden studio floor set with mats, blocks and towels">
      <path d="M0 566 L924 348 L1200 320 L1200 800 L0 800 Z" fill="url(#studio-tone)"/>
    </g>
    <path class="swoosh swoosh--sky" d="M760 0 C700 90 690 230 830 330 C960 420 1020 580 960 800 L1080 800 C1130 580 1070 400 930 300 C820 220 800 90 870 0 Z" fill="var(--sky)"/>
    <path class="swoosh swoosh--deep" d="M1000 325 C1110 335 1182 430 1182 570 L1178 800 L1110 800 C1125 620 1085 430 1000 325 Z" fill="var(--deep)"/>
    <path d="M1182 570 L1178 800 L1200 800 L1200 330 C1190 400 1182 480 1182 570 Z" fill="var(--paper)"/>
  </svg>

  <div class="rule rule--top"></div>
  <section class="contact">
    <p class="contact__web">www.amberlilyyoga.com.au</p>
    <p class="contact__find">or find us at
      <span class="contact__channel">classora</span>
      <span class="contact__channel">linkhive</span>
      <span class="contact__channel">pixly</span>
    </p>
  </section>
  <div class="rule rule--bottom"></div>

  <p class="brand">AMBER LILY<br>YOGA</p>

  <div class="portrait" role="img" aria-label="Portrait photo of the studio's yoga teacher"></div>
  <ul class="values">
    <li class="values__item">Strengthen your well-being through adaptive yoga.</li>
    <li class="values__item">Seek to evolve your mind and body through the challenge of yoga.</li>
    <li class="values__item">Perfection is a desire and never an outcome through the practice of yoga.</li>
  </ul>
  <p class="vision">Our vision is to create an atmosphere that enables inclusiveness of the whole community.</p>

  <p class="invite">Come join us!</p>

  <h1 class="headline">
    <span class="headline__lead">ENABLE</span>
    <span class="headline__sub">FUNCTIONAL</span>
    <span class="headline__sub">WELLBEING</span>
  </h1>
</main>
</body>
</html>
```